New National Dermatology Group needs a business card!

We need a business card for our new national company that has 3 brands within the business:
Brellow Clinics Australia, Tamvirk Clinics Australia and Orvandel Clinics Australia.
We help people access dermatology services close to home throughout Australia.
We need a business card that has:
all 3 logos on it,
Our websites (there are three, listed above)
Our email (there are three, listed above)
The location of our first clinic: 41 Wendle St Parramatta (this can then be changed for each location as required)

```html
<!DOCTYPE html>
<html lang="en">
<head>
<meta charset="utf-8">
<title>Brellow, Tamvirk &amp; Orvandel Clinics Australia – Business Card</title>
<link rel="stylesheet" href="https://fonts.googleapis.com/css2?family=Arimo:wght@400;700&display=swap">
<style>
  :root {
    --page-bg: #d9d9d9;
    --card-sky: #a9dcf1;
    --card-mist: #e6f4fb;
    --card-white: #ffffff;
    --ink: #4a4a4a;
    --ink-soft: #6b6b6b;
    --rule: #9a9a9a;
    --brand-green: #2f9a45;
    --brand-orange: #e9832c;
    --brand-brown: #7a3b17;
    --brand-grey: #555555;
    --pattern-blue: #8fd0ee;
    --pattern-pale: #d6eef9;
  }
  * { box-sizing: border-box; margin: 0; padding: 0; }
  html, body {
    width: 1200px; height: 848px; overflow: hidden;
    background: var(--page-bg);
    font-family: "Arimo", Arial, sans-serif;
    color: var(--ink);
  }
  .canvas {
    position: relative; width: 1200px; height: 848px;
    display: flex; align-items: center; justify-content: center; gap: 40px;
  }
  .card {
    position: relative; width: 540px; height: 310px; overflow: hidden;
    background: linear-gradient(160deg, var(--card-sky) 0%, var(--card-mist) 45%, var(--card-white) 85%);
    box-shadow: 0 4px 14px rgba(0,0,0,0.12);
  }
  .pattern {
    position: absolute;
    background: radial-gradient(ellipse at center, var(--pattern-blue) 0%, var(--pattern-pale) 45%, rgba(214,238,249,0) 75%);
    opacity: 0.85;
  }
  .card--front .pattern--top { top: -40px; right: -40px; width: 300px; height: 200px; }
  .card--front .pattern--corner { bottom: -50px; left: 90px; width: 200px; height: 110px; opacity: 0.6; }
  .card--back .pattern--top { top: -60px; left: 120px; width: 480px; height: 260px; }

  .email-list { position: absolute; left: 36px; top: 70px; list-style: none; }
  .email-list li {
    display: flex; align-items: center; gap: 10px;
    font-size: 16px; line-height: 28px; color: var(--ink);
  }
  .email-list li:nth-child(2) { padding-left: 18px; }
  .email-list li:nth-child(3) { padding-left: 36px; }
  .mail-icon { width: 22px; height: 22px; flex: none; }

  .brand-row {
    position: absolute; left: 60px; right: 28px;
    display: flex; justify-content: space-between; align-items: flex-start;
  }
  .brand-name {
    display: block; width: 132px;
    font-size: 14px; line-height: 17px; font-weight: 700; letter-spacing: 0.02em;
  }
  .brand-name--green { color: var(--brand-green); }
  .brand-name--orange { color: var(--brand-orange); }
  .brand-name--brown { color: var(--brand-brown); }
  .brand-name--grey { color: var(--brand-grey); }

  .card--front .brand-row { top: 168px; }
  .divider { position: absolute; left: 60px; right: 28px; top: 216px; height: 1px; background: var(--rule); }
  .address { position: absolute; left: 100px; top: 230px; font-size: 16px; color: var(--ink); }

  .web-list { position: absolute; left: 36px; top: 150px; list-style: none; }
  .web-list li { font-size: 15px; line-height: 24px; color: var(--ink-soft); }
  .web-list li:nth-child(2) { padding-left: 18px; }
  .web-list li:nth-child(3) { padding-left: 36px; }
  .card--back .brand-row { top: 240px; }
</style>
</head>
<body>
<main class="canvas">

  <section class="card card--front" aria-label="Business card front">
    <div class="pattern pattern--top" role="img" aria-label="Soft blue molecular hexagon network decoration"></div>
    <div class="pattern pattern--corner" role="img" aria-label="Faint blue hexagon network decoration"></div>

    <ul class="email-list">
      <li>
        <svg class="mail-icon" viewBox="0 0 22 22" aria-hidden="true">
          <circle cx="11" cy="11" r="10" fill="var(--brand-green)"/>
          <rect x="5.5" y="7" width="11" height="8" fill="none" stroke="#fff" stroke-width="1.4"/>
          <polyline points="5.5,7 11,11.5 16.5,7" fill="none" stroke="#fff" stroke-width="1.4"/>
        </svg>
        name@brellowclinicsaustralia.com.au
      </li>
      <li>
        <svg class="mail-icon" viewBox="0 0 22 22" aria-hidden="true">
          <circle cx="11" cy="11" r="10" fill="var(--brand-orange)"/>
          <rect x="5.5" y="7" width="11" height="8" fill="none" stroke="#fff" stroke-width="1.4"/>
          <polyline points="5.5,7 11,11.5 16.5,7" fill="none" stroke="#fff" stroke-width="1.4"/>
        </svg>
        name@brellowclinicsaustralia.com.au
      </li>
      <li>
        <svg class="mail-icon" viewBox="0 0 22 22" aria-hidden="true">
          <circle cx="11" cy="11" r="10" fill="var(--brand-brown)"/>
          <rect x="5.5" y="7" width="11" height="8" fill="none" stroke="#fff" stroke-width="1.4"/>
          <polyline points="5.5,7 11,11.5 16.5,7" fill="none" stroke="#fff" stroke-width="1.4"/>
        </svg>
        name@brellowclinicsaustralia.com.au
      </li>
    </ul>

    <div class="brand-row">
      <span class="brand-name brand-name--green">Brellow Clinics Australia</span>
      <span class="brand-name brand-name--orange">Tamvirk Clinics Australia</span>
      <span class="brand-name brand-name--brown">Orvandel Clinics Australia</span>
    </div>
    <div class="divider"></div>
    <p class="address">41 Wendle St, Parramatta, NSW 2150, Sydney</p>
  </section>

  <section class="card card--back" aria-label="Business card back">
    <div class="pattern pattern--top" role="img" aria-label="Soft blue molecular hexagon network decoration"></div>

    <ul class="web-list">
      <li>www.brellowclinicsaustralia.com.au</li>
      <li>www.brellowclinicsaustralia.com.au</li>
      <li>www.brellowclinicsaustralia.com.au</li>
    </ul>

    <div class="brand-row">
      <span class="brand-name brand-name--grey">Brellow Clinics Australia</span>
      <span class="brand-name brand-name--grey">Tamvirk Clinics Australia</span>
      <span class="brand-name brand-name--grey">Orvandel Clinics Australia</span>
    </div>
  </section>

</main>
</body>
</html>
```